Milo Fenwick - Cinematographer

NEED:
I'm looking for a sleek, professional, modern business card that will give give the recipient the impression that they can trust their production will go smoothly by hiring me. I will bring creativity and knowledge to their shoot, so that we can create powerful images.
I am looking for a card with a strong style and design ethos that could be expanded to a website and a full visual/graphic/design entity for me.
ABOUT ME:
I am a mid-twenties cinematographer, I work on music video, narrative short, commercial, and corporate projects. I blend the science and artistry of cameras and filmmaking to tell a story. I'm an artist, a technician, and a manager.
DESIGN:
I like sleek, simple design. Black, dark grays, white, dark navy, steel blues, I love cyan, but also cyan and red. I am not a fan of earthy tones. I generally prefer modern, san-serif fonts over serifs. My old logo was based on an aperture, a multi-blade device at the back of a lens that controls how much light passes through, but I made it with so many colors, that it doesn't necessarily lend itself to a specific color-scheme or design ethos. I liked that the aperture design provided a sense of the technical requirements of my job. I'm a fan of matte business cards, but am open to plenty of specialty print processes to make an outstanding card.
ATTACHED FILES:
My Old Rainbox Aperture Logo, plus a few designs I've tried playing around with, but am not tied to. I AM OPEN TO NEW DESIGNS, DO NOT FEEL TIED TO THIS.
**I've pulled my old logo down from the attached files, and instead attached other business cards I like, so as not to mislead you where I would like to go.
INFO:
Name: Milo Fenwick
Job: Cinematographer
Email: mpfenwick@quellbox.net
Phone: 415.555.0193
Website: milofenwick.net
I'm adding some images of other cards that I like, and removing my old logo, since I'm looking for something new, and don't want that old logo to push anyone a certain direction.

```html
<!DOCTYPE html>
<html lang="en">
<head>
<meta charset="utf-8">
<title>Milo Fenwick – Cinematographer Business Card</title>
<link rel="stylesheet" href="https://fonts.googleapis.com/css2?family=Saira+Condensed:wght@500;600;700&display=swap">
<style>
  :root {
    --page-bg: #e6e7e9;
    --card-black: #0b0b0c;
    --card-black-soft: #1a1b1d;
    --ink-white: #f4f5f6;
    --cyan: #5ccdf5;
    --cyan-deep: #3fbfee;
    --rule-grey: #b9bcc0;
  }
  * { margin: 0; padding: 0; box-sizing: border-box; }
  html, body {
    width: 1000px;
    height: 1200px;
    overflow: hidden;
    background: var(--page-bg);
  }
  .canvas {
    position: relative;
    width: 1000px;
    height: 1200px;
  }
  .card {
    position: absolute;
    left: 70px;
    width: 860px;
    height: 491px;
    background: linear-gradient(180deg, var(--card-black) 0%, var(--card-black-soft) 100%);
    color: var(--ink-white);
    overflow: hidden;
    box-shadow: 0 10px 28px rgba(0, 0, 0, 0.25);
    font-family: "Saira Condensed", "Arial Narrow", sans-serif;
  }
  .card--front { top: 70px; }
  .card--back { top: 639px; background: var(--card-black); }

  /* Front */
  .front__title {
    position: absolute;
    left: 66px;
    top: 74px;
    font-size: 66px;
    font-weight: 700;
    line-height: 1;
    text-transform: uppercase;
    letter-spacing: 1px;
    white-space: nowrap;
  }
  .front__title-initial {
    color: var(--cyan);
    font-size: 88px;
  }
  .front__rule {
    position: absolute;
    height: 2px;
    background: var(--rule-grey);
  }
  .front__rule--upper { left: 50px; top: 162px; width: 510px; }
  .front__rule--lower { left: 0; top: 184px; width: 620px; }
  .front__rule--tail { left: 830px; top: 184px; width: 30px; }

  .name-mark {
    position: absolute;
    display: flex;
    align-items: center;
    gap: 12px;
    font-family: "Saira Condensed", "Arial Narrow", sans-serif;
    font-weight: 600;
    color: var(--ink-white);
    text-transform: uppercase;
    line-height: 0.95;
    white-space: nowrap;
  }
  .name-mark__dot {
    flex: none;
    border-radius: 50%;
    background: var(--ink-white);
  }
  .front .name-mark { left: 650px; top: 144px; font-size: 40px; }
  .front .name-mark__dot { width: 12px; height: 12px; }

  .front__contact {
    position: absolute;
    left: 80px;
    top: 226px;
    text-transform: uppercase;
    font-family: "Saira Condensed", "Arial Narrow", sans-serif;
    font-weight: 600;
  }
  .front__phone { font-size: 44px; line-height: 1.05; letter-spacing: 1px; }
  .front__email, .front__web { font-size: 32px; line-height: 1.15; letter-spacing: 2px; }
  .front__email-domain { color: var(--cyan); }

  .front__services {
    position: absolute;
    left: 80px;
    top: 362px;
    font-size: 31px;
    font-weight: 600;
    line-height: 1.2;
    text-transform: uppercase;
  }
  .front__divider { color: var(--cyan); padding: 0 8px; }

  .front__band {
    position: absolute;
    left: 0;
    bottom: 0;
    width: 100%;
    height: 50px;
    background: linear-gradient(180deg, var(--cyan) 0%, var(--cyan-deep) 100%);
  }

  /* Back */
  .back .name-mark {
    left: 0;
    right: 0;
    top: 130px;
    justify-content: center;
    font-size: 56px;
  }
  .back .name-mark__dot { width: 16px; height: 16px; }
  .back__title {
    position: absolute;
    left: 0;
    right: 0;
    top: 300px;
    text-align: center;
    font-size: 64px;
    font-weight: 600;
    letter-spacing: 5px;
    text-transform: uppercase;
  }
</style>
</head>
<body>
<main class="canvas">

  <section class="card card--front front" aria-label="Business card front">
    <h1 class="front__title"><span class="front__title-initial">C</span>inematographer</h1>
    <div class="front__rule front__rule--upper"></div>
    <div class="front__rule front__rule--lower"></div>
    <div class="front__rule front__rule--tail"></div>

    <div class="name-mark">
      <span class="name-mark__text">Milo<br>Fenwick</span>
      <span class="name-mark__dot"></span>
    </div>

    <div class="front__contact">
      <p class="front__phone">415.555.0193</p>
      <p class="front__email">mpfenwick@<span class="front__email-domain">quellbox.net</span></p>
      <p class="front__web">milofenwick.net</p>
    </div>

    <p class="front__services">
      Music Video<span class="front__divider">|</span>Narrative Short<span class="front__divider">|</span>Commercial<br>
      Corporate Projects
    </p>

    <div class="front__band"></div>
  </section>

  <section class="card card--back back" aria-label="Business card back">
    <div class="name-mark">
      <span class="name-mark__text">Milo Fenwick</span>
      <span class="name-mark__dot"></span>
    </div>
    <p class="back__title">Cinematographer</p>
  </section>

</main>
</body>
</html>
```